Craft oriented film company needs a Business Card design

Hi all,
We're a 2-man band film company in New Zealand called Brindle Pictures. We're good honest blokes, who are very passionate about the craft of film making. I've attached our current logo which has a bit of a crafty/artisan feel that we like. Feel free to use it - or throw the baby out with the bathwater and start again..... you never know, you might inspire a complete brand re-work.

In any case, the vibe we want to give out is that we are solid, dependable and no bullshit - but without compromising creative excellence and being in the now. We like the 'Brooklyn' artisan style of work.

Preferably single sided.

We need the standard stuff:
Name, job title, cellphone, email address and physical address (this can be smaller if you like - street, suburb, city & zip, country [if you want])

Check out our website to learn more about us: brindlepictures.example

Target Market(s)

Brand marketers and advertising agency creatives looking for video production.

Requirements
Should not have
• Nothing flashy or too 'futuristic', we want it to feel grounded and real. A limited colour palette is preferred.
We don't want any film reels or cameras or anything obvious like that.

```html
<!DOCTYPE html>
<html lang="en">
<head>
<meta charset="utf-8">
<title>Brindle Pictures – Business Card</title>
<link rel="stylesheet" href="https://fonts.googleapis.com/css2?family=Hind:wght@400;500&display=swap">
<style>
  :root {
    --backdrop: #e4e1da;
    --card-paper: #f7f6ef;
    --ink: #0d0d0d;
  }
  * { margin: 0; padding: 0; box-sizing: border-box; }
  html, body {
    width: 1200px;
    height: 749px;
    overflow: hidden;
    background: var(--backdrop);
  }
  .business-card {
    position: absolute;
    left: 274px;
    top: 184px;
    width: 652px;
    height: 382px;
    background: var(--card-paper);
    color: var(--ink);
    font-family: "Hind", sans-serif;
    box-shadow: 0 2px 6px rgba(0,0,0,0.18);
    overflow: hidden;
  }
  .side-band {
    position: absolute;
    left: 0; top: 0;
    width: 76px; height: 100%;
    background: var(--ink);
  }
  .side-rule {
    position: absolute;
    left: 78px; top: 0;
    width: 4px; height: 100%;
    background: var(--ink);
  }
  .brand {
    position: absolute;
    left: 154px;
    top: 150px;
    width: 160px;
    text-align: center;
  }
  .brand-dot {
    display: block;
    width: 30px; height: 30px;
    margin: 0 auto 10px;
    border-radius: 50%;
    background: var(--ink);
  }
  .brand-name {
    font-size: 19px;
    font-weight: 500;
    letter-spacing: 1.5px;
    line-height: 1.2;
    text-transform: uppercase;
  }
  .contact-block {
    position: absolute;
    left: 383px;
    top: 72px;
  }
  .person-name {
    font-size: 26px;
    font-weight: 500;
    letter-spacing: 1px;
    line-height: 1;
    text-transform: uppercase;
  }
  .person-role {
    margin-top: 8px;
    font-size: 18px;
    font-weight: 400;
    letter-spacing: 0.8px;
    line-height: 1;
    text-transform: uppercase;
  }
  .contact-list {
    list-style: none;
    margin-top: 22px;
    font-size: 15.5px;
    line-height: 22.5px;
  }
  .contact-item {
    position: relative;
    padding-left: 28px;
  }
  .contact-item.address { margin-top: 18px; }
  .contact-icon {
    position: absolute;
    left: 0;
    top: 5px;
    width: 14px;
    height: 12px;
    fill: var(--ink);
  }
</style>
</head>
<body>
  <article class="business-card">
    <div class="side-band"></div>
    <div class="side-rule"></div>

    <div class="brand">
      <span class="brand-dot"></span>
      <p class="brand-name">Brindle Pictures</p>
    </div>

    <section class="contact-block">
      <h1 class="person-name">Rowan Hale</h1>
      <p class="person-role">Producer</p>
      <ul class="contact-list">
        <li class="contact-item">
          <svg class="contact-icon" viewBox="0 0 14 12" aria-hidden="true">
            <path d="M1 5 C1 2 13 2 13 5 L13 6.5 L10 6.5 L10 5 C9 4.3 5 4.3 4 5 L4 6.5 L1 6.5 Z"/>
            <rect x="3" y="7.5" width="8" height="2.5" rx="0.5"/>
          </svg>
          +64-21-555-017
        </li>
        <li class="contact-item">
          <svg class="contact-icon" viewBox="0 0 14 12" aria-hidden="true">
            <path d="M1 2 H13 V10 H1 Z M1.8 2.6 L7 6.6 L12.2 2.6" stroke="#f7f6ef" stroke-width="1"/>
          </svg>
          rowan@brindlepictures.example
        </li>
        <li class="contact-item address">
          <svg class="contact-icon" viewBox="0 0 14 12" aria-hidden="true">
            <path d="M7 0.5 C4.6 0.5 3.3 2.2 3.3 4 C3.3 6.5 7 11.5 7 11.5 C7 11.5 10.7 6.5 10.7 4 C10.7 2.2 9.4 0.5 7 0.5 Z M7 2.6 A1.4 1.4 0 1 1 7 5.4 A1.4 1.4 0 1 1 7 2.6 Z" fill-rule="evenodd"/>
          </svg>
          Address line street,<br>
          Address line suburb,<br>
          City &amp; zip,<br>
          Country
        </li>
      </ul>
    </section>
  </article>
</body>
</html>
```